Dane Morrow films- wedding and event films company website. DESKTOP AND MOBILE

We need a website for a high-end wedding and event film production company. Looking for a very modern and elegant design. my old website is www.danemorrowfilms.example

I like the "white/black/rose gold" color scheme of my logo.

really looking for a sleek modern design the breaths professional and artistic.

Target Market(s)

wedding and event films.

Industry/Entity Type

Film Production

Number of Pages Required

5+ page

Colors

Designer to choose colors to be used in the design.

Requirements
Must have
• website name will be www.danemorrowfilms.example
• tagline is "CINEMATIC STORIES ABOUT YOU"
• sections: HOME, CONTACT, ABOUT, FILMS, BLOG
• You can see my old website at danemorrowfilms.example
• Website about section:
• Dane Morrow Films was Established with the basis of truly cinematic and artistic films in mind. Dane and his team routinely travel the globe documenting weddings and events for high profile clients and discerning couples. Dane was born and raised in Maui Hawaii and has a unique approach to his films that embody the essence of a Hollywood film. Dane has spent the last 10 years traveling the world documenting corporate events and weddings with multiple Award winning production companies. In 2017 Dane decided to establish his own brand “Dane Morrow films” that will take everything he has learned with his past experiences and push it to the next level. Aside from his personal achievements, Dane is extremely passionate about his craft and always looks forward to handcrafting beautiful wedding/event films for his clients. The style of work is non-traditional and the day of filming is extremely unobtrusive (as we are looking for natural-candid/ raw emotions).
• If you are looking for the best price in town, we are probably not the best option, but if you’re looking for the best quality and peace of mind on your wedding day, then you’re in the right place. Dane Morrow Films is a boutique studio that only accepts a limited number of assignments per year. Inquire early to ensure availability.
• LINKS TO VIMEO VIDEOS THAT WILL BE IN THE "FILMS' SECTION.
• BRENT FILM TRAILER - https://clipvault.example/508114362
• BRENT FEATURE FILM - https://clipvault.example/617392048
• JUNE AND ROB'S WEDDING - https://clipvault.example/724958160
• DRONE DEMO REEL - https://clipvault.example/841576203
• WEDDING INDUSTRY EVENT PARTY - https://clipvault.example/962304817/a8d3e7b21c
• images that you can use on site are here: https://brigittolsenimages.proofbox.example/gallery/nora&felix/
• password is: meadow

```html
<!DOCTYPE html>
<html lang="en">
<head>
<meta charset="utf-8">
<title>Dane Morrow Films</title>
<link href="https://fonts.googleapis.com/css2?family=Source+Sans+3:wght@400;600;700&display=swap" rel="stylesheet">
<style>
:root{
  --accent:#d98b4f;
  --ink:#1c1c1c;
  --muted:#6f6f6f;
  --line:#d8d8d8;
  --footer:#9b9b9b;
  --white:#ffffff;
  --hero-a:#3a3835;
  --hero-b:#7b766f;
}
*{margin:0;padding:0;box-sizing:border-box}
html,body{width:1200px;height:2185px;overflow:hidden;background:var(--white)}
body{position:relative;font-family:"Source Sans 3",Arial,sans-serif;color:var(--ink)}
.abs{position:absolute}
.site-header{left:0;top:0;width:1200px;height:70px;background:var(--white)}
.brand{left:212px;top:14px;display:flex;align-items:center;gap:8px}
.brand-mark{width:14px;height:14px;background:var(--accent)}
.brand-name{font-size:15px;font-weight:600;letter-spacing:1px;color:var(--ink);line-height:1}
.brand-sub{display:block;font-size:8px;letter-spacing:4px;color:var(--accent);margin-top:3px}
.main-nav{top:33px;display:flex;gap:0}
.main-nav a{position:absolute;font-size:10px;color:var(--accent);text-decoration:none;white-space:nowrap}
.main-nav a.active::after{content:"";position:absolute;left:-3px;right:-3px;bottom:-6px;height:1px;background:var(--accent)}
.hero{left:0;top:70px;width:1200px;height:204px;background:linear-gradient(90deg,#5b5853,#8a847c 30%,#4a4743 55%,#2c2a28)}
.hero-title{left:0;top:151px;width:1200px;text-align:center;color:var(--white);font-size:20px;line-height:24px;font-weight:600}
.intro-title{left:0;top:333px;width:1200px;text-align:center;color:var(--accent);font-size:20px;font-weight:600}
.intro-sub{left:0;top:365px;width:1200px;text-align:center;font-size:12px}
.intro-text{left:340px;top:410px;width:520px;text-align:center;font-size:9.5px;line-height:19px;color:var(--ink)}
.photo{background:linear-gradient(135deg,#f0c48a,#c7744a 55%,#6e3326)}
.photo-feature{left:195px;top:499px;width:818px;height:277px}
.slider-bar{left:552px;top:776px;width:461px;height:27px;background:var(--white);border-left:2px solid var(--line);border-bottom:2px solid var(--line)}
.dots{left:14px;top:10px;display:flex;gap:6px}
.dots i{width:7px;height:7px;border-radius:50%;background:var(--line)}
.dots i:first-child{background:var(--accent)}
.view-more{font-size:8.5px;font-weight:600;color:var(--accent);display:flex;align-items:center;gap:8px;white-space:nowrap}
.plus{width:13px;height:13px;border:1px solid var(--ink);border-radius:50%;position:relative}
.plus::before,.plus::after{content:"";position:absolute;background:var(--ink);left:50%;top:50%;transform:translate(-50%,-50%)}
.plus::before{width:7px;height:1px}.plus::after{width:1px;height:7px}
.ceremony-icon{left:212px;top:830px}
.ceremony-title{left:212px;top:862px;font-size:23px;line-height:26px;font-weight:400}
.ceremony-title span{display:block;color:var(--accent);font-size:18px;line-height:22px}
.ceremony-text{left:212px;top:930px;width:200px;font-size:8.5px;line-height:16px;color:var(--ink)}
.photo-ceremony{left:436px;top:818px;width:577px;height:253px;background:linear-gradient(180deg,#b9b2a8,#8b8378 50%,#4f4a44)}
.ceremony-bar{left:480px;top:1071px;width:460px;height:29px;background:var(--white);border-left:2px solid var(--line);border-right:2px solid var(--line);border-bottom:2px solid var(--line)}
.ceremony-bar .view-more{left:15px;top:8px}
.bar-note{right:8px;top:9px;font-size:8.5px;color:var(--ink)}
.photo-left{left:193px;top:1149px;width:344px;height:288px;background:linear-gradient(180deg,#a9b3bd,#7b848c 45%,#3a3f4a)}
.photo-right{left:556px;top:1149px;width:457px;height:344px;background:linear-gradient(135deg,#fbeee0,#efd4bb 60%,#e2bea0)}
.project-card{left:448px;top:1266px;width:234px;height:266px;background:var(--white);border:3px solid #e4e4e4;border-top:none;border-left:4px solid #e4e4e4}
.project-card h2{position:absolute;left:30px;top:64px;font-size:21px;line-height:24px;font-weight:600}
.project-card p{position:absolute;left:32px;top:136px;width:175px;font-size:8.5px;line-height:15.5px;color:var(--muted)}
.client-heading{left:522px;top:1578px;font-size:21px;font-weight:600;letter-spacing:.5px}
.client-photo{left:334px;top:1601px;width:136px;height:142px;background:linear-gradient(135deg,#f4f1ec,#e3d8cb)}
.client-name{left:518px;top:1625px;font-size:20px}
.client-text{left:518px;top:1669px;width:420px;font-size:8.5px;line-height:16px;color:var(--muted)}
.contact{left:0;top:1781px;width:1200px;height:303px;background:var(--footer);color:var(--white)}
.contact h2{position:absolute;left:224px;top:33px;font-size:16px;font-weight:400}
.contact-line{position:absolute;left:234px;display:flex;align-items:center;gap:12px;font-size:8.5px}
.follow{position:absolute;left:224px;top:172px;font-size:8.5px;font-weight:600}
.socials{position:absolute;left:224px;top:204px;display:flex;gap:10px;font-size:8px}
.field{position:absolute;font-size:8.5px;font-weight:600;border-bottom:1px solid #b3b3b3;padding-bottom:14px}
.submit{position:absolute;left:497px;top:238px;width:107px;height:31px;background:var(--accent);color:var(--white);font-size:9.5px;font-weight:600;display:flex;align-items:center;justify-content:center}
.legal{left:0;top:2084px;width:1200px;height:101px}
.legal-links{position:absolute;left:0;top:36px;width:1200px;text-align:center;font-size:7.5px;color:var(--ink);letter-spacing:2px}
.copyright{position:absolute;left:0;top:60px;width:1200px;text-align:center;font-size:8.5px;color:var(--muted)}
</style>
</head>
<body>

<header class="site-header abs">
  <div class="brand abs">
    <span class="brand-mark"></span>
    <span class="brand-name">DANE MORROW<span class="brand-sub">FILMS</span></span>
  </div>
  <nav class="main-nav abs">
    <a class="active" href="#" style="left:685px">Home</a>
    <a href="#" style="left:729px">About</a>
    <a href="#" style="left:771px">Films</a>
    <a href="#" style="left:808px">Blogs</a>
    <a href="#" style="left:847px">Contact</a>
  </nav>
  <svg class="abs" style="left:898px;top:33px" width="13" height="13" viewBox="0 0 13 13" fill="none" stroke="#d98b4f" stroke-width="1.3"><circle cx="5.5" cy="5.5" r="4.3"/><path d="M8.6 8.6L12 12"/></svg>
</header>

<section class="hero abs" role="img" aria-label="Black and white photo of a laughing wedding couple"></section>
<h1 class="hero-title abs">Dane Morrow<br>Theater</h1>

<h2 class="intro-title abs">Wedding</h2>
<p class="intro-sub abs">Cinematic Storry Films</p>
<p class="intro-text abs">At Dane Morrow Films we specialize in offering the finest in wedding and corporate cinematography. We offer a very modern and creative style for capturing your special moments with a beautiful and cinematic approach that enables up to produce the highest quality of films. Dane and his hand selected team have over 10 years of experience, and they strive to make the best films i</p>

<div class="photo photo-feature abs" role="img" aria-label="Bride and groom embracing at sunset"></div>
<div class="slider-bar abs">
  <div class="dots abs"><i></i><i></i><i></i><i></i></div>
  <div class="view-more abs" style="left:110px;top:7px">View More <span class="plus"></span></div>
</div>

<svg class="ceremony-icon abs" width="24" height="22" viewBox="0 0 24 22" fill="none" stroke="#8a8a8a" stroke-width="1.2"><rect x="1" y="4" width="22" height="17"/><path d="M4 1h16"/><path d="M10 9l6 3.5-6 3.5z"/></svg>
<h2 class="ceremony-title abs">WEDDING<span>ceremony</span></h2>
<p class="ceremony-text abs">If you are looking for the best price in town, we are probably not the best option, but if you’re looking for the best quality and peace of mind on your wedding day, then you’re in the right place</p>

<div class="photo-ceremony abs" role="img" aria-label="Groom dipping bride on a rocky seaside coast"></div>
<svg class="abs" style="left:436px;top:818px" width="577" height="253" viewBox="0 0 577 253" fill="none" stroke="#fff" stroke-width="2">
  <circle cx="299" cy="120" r="20"/><path d="M293 110l16 10-16 10z"/>
  <path d="M14 124h18M14 124l6-6M14 124l6 6"/>
  <path d="M545 118h18M563 118l-6-6M563 118l-6 6"/>
</svg>
<div class="ceremony-bar abs">
  <div class="view-more abs">View More <span class="plus"></span></div>
  <span class="bar-note abs">link to vimeos that will be the Films Sections</span>
</div>

<div class="photo-left abs" role="img" aria-label="Groom walking by a seaside railing"></div>
<svg class="abs" style="left:357px;top:1264px" width="42" height="42" viewBox="0 0 42 42" fill="none" stroke="#fff" stroke-width="2"><circle cx="21" cy="21" r="19"/><path d="M16 12l13 9-13 9z"/></svg>
<div class="view-more abs" style="left:209px;top:1456px">View More <span class="plus"></span></div>

<div class="photo-right abs" role="img" aria-label="Portrait of a smiling groom in a white shirt"></div>
<svg class="abs" style="left:708px;top:1460px" width="60" height="16" viewBox="0 0 60 16" fill="none" stroke="#1c1c1c" stroke-width="1.6"><path d="M2 8h18M2 8l6-6M2 8l6 6"/><path d="M38 8h18M56 8l-6-6M56 8l-6 6"/></svg>
<div class="view-more abs" style="left:711px;top:1508px">View More <span class="plus"></span></div>

<article class="project-card abs">
  <svg class="abs" style="left:26px;top:26px" width="32" height="14" viewBox="0 0 32 14" fill="none" stroke="#555" stroke-width="1"><circle cx="7" cy="7" r="6"/><path d="M5 4l5 3-5 3z"/><rect x="19" y="1" width="12" height="12"/><path d="M19 5h12"/><circle cx="25" cy="9" r="2"/></svg>
  <h2>Latest Wedding Projects</h2>
  <p>Dane Morrow Films was Established with the basis of truly cinematic and artistic films in mind. Dane and his team routinely travel the globe documenting weddings and events</p>
</article>

<h2 class="client-heading abs">OUR CLIENT</h2>
<svg class="abs" style="left:214px;top:1669px" width="18" height="14" viewBox="0 0 18 14" fill="none" stroke="#1c1c1c" stroke-width="1.6"><path d="M1 7h16M1 7l6-6M1 7l6 6"/></svg>
<div class="client-photo abs" role="img" aria-label="Portrait of a smiling client"></div>
<p class="client-name abs">Liam Harte</p>
<p class="client-text abs">Dane Morrow Films was Established with the basis of truly cinematic and artistic films in mind. Dane and his team routinely travel the globe documenting weddings and events</p>
<svg class="abs" style="left:964px;top:1669px" width="18" height="14" viewBox="0 0 18 14" fill="none" stroke="#1c1c1c" stroke-width="1.6"><path d="M1 7h16M17 7l-6-6M17 7l-6 6"/></svg>

<section class="contact abs">
  <h2>Contact Us</h2>
  <div class="contact-line" style="top:100px">
    <svg width="14" height="14" viewBox="0 0 14 14" fill="none" stroke="#d98b4f" stroke-width="1.3"><path d="M3 1l3 3-2 2c1 2 2 3 4 4l2-2 3 3-2 2C6 13 1 8 1 3z"/></svg>
    <span>+567 555 010 482</span>
  </div>
  <div class="contact-line" style="top:132px">
    <svg width="16" height="12" viewBox="0 0 16 12" fill="none" stroke="#d98b4f" stroke-width="1.3"><rect x="1" y="1" width="14" height="10"/><path d="M1 1l7 6 7-6"/></svg>
    <span>hello@danemorrowfilms.example</span>
  </div>
  <p class="follow">Follow US:</p>
  <div class="socials"><span>Share</span><span>Follow</span><span>Gallery</span></div>

  <div class="field" style="left:508px;top:69px;width:194px">Name</div>
  <div class="field" style="left:746px;top:69px;width:195px">Email</div>
  <div class="field" style="left:508px;top:105px;width:194px">Phone</div>
  <div class="field" style="left:746px;top:104px;width:195px">Subject</div>
  <div class="field" style="left:508px;top:146px;width:433px;padding-bottom:36px">Message</div>
  <div class="submit">Submit</div>
</section>

<footer class="legal abs">
  <p class="legal-links">Share · Follow · Gallery</p>
  <p class="copyright">Copyright © 2017 Dane Morrow. All right reserved.</p>
</footer>

</body>
</html>
```